Social Media Post – Promotion Announcement for Marcus Holloway

Objective:
Create a professional and eye-catching social media post announcing the promotion of Marcus Holloway to Vice President of Sales – Foodservice. The design should be modern, clean, and aligned with Brenwick Sales & Marketing’s branding style (friendly, West Coast, professional). It should match our website:

www.brenwicksales.example

Key Requirements:

Include Marcus Holloway’s photo (we will provide a high-resolution image).
Prominently display his name: “Marcus Holloway.”
Prominently display his new title: “Vice President of Sales – Foodservice.”

A header or highlight that says something like: “Promotion Announcement” or “Congratulations!”

Design must be editable in Canva so we can reuse the template for future promotions.

Square format (1080x1080px) for Instagram/LinkedIn, but adaptable to landscape (1200x628px) if possible.

Style Guide / Preferences:

Colors: Incorporate Brenwick Sales & Marketing brand blue (#0B64C0) along with white, gray, and/or complementary tones.

Fonts: Clean, modern sans-serif. Readable even on mobile.

Layout: Balanced between photo and text.

Option 1: Circular frame for the photo at center/top, text below.

Option 2: Split design with photo on one side and text on the other.

Tone: Professional, celebratory, approachable.

Deliverables:

Canva template file (editable).

Exported PNG/JPEG preview for review.

```html
<!DOCTYPE html>
<html lang="en">
<head>
<meta charset="utf-8">
<title>Promotion Announcement – Marcus Holloway</title>
<link rel="stylesheet" href="https://fonts.googleapis.com/css2?family=Montserrat:wght@600;700;800&family=Yellowtail&display=swap">
<style>
  :root {
    --brand-blue: #3553a4;
    --brand-yellow: #fdbd17;
    --title-gray: #8f8f8f;
    --paper: #ffffff;
    --photo-dark: #4a3a30;
    --photo-mid: #7d8a9c;
  }
  html, body {
    margin: 0;
    padding: 0;
    width: 1200px;
    height: 1200px;
    overflow: hidden;
    background: var(--paper);
  }
  .post {
    position: relative;
    width: 1200px;
    height: 1200px;
    overflow: hidden;
    background: var(--paper);
    font-family: "Montserrat", Arial, sans-serif;
  }
  .post__swoosh {
    position: absolute;
    inset: 0;
    width: 1200px;
    height: 1200px;
  }
  .post__headline {
    position: absolute;
    top: 10px;
    left: 0;
    width: 100%;
    margin: 0;
    text-align: center;
    white-space: nowrap;
    font-family: "Yellowtail", "Brush Script MT", cursive;
    font-weight: 400;
    font-size: 132px;
    line-height: 1.2;
    color: var(--brand-yellow);
  }
  .post__name {
    position: absolute;
    top: 192px;
    left: 0;
    width: 100%;
    margin: 0;
    text-align: center;
    white-space: nowrap;
    font-weight: 800;
    font-size: 90px;
    line-height: 1.1;
    letter-spacing: 0;
    color: var(--brand-blue);
    text-transform: uppercase;
  }
  .post__title {
    position: absolute;
    top: 322px;
    left: 0;
    width: 100%;
    margin: 0;
    text-align: center;
    white-space: nowrap;
    font-weight: 700;
    font-size: 40px;
    letter-spacing: 1px;
    color: var(--title-gray);
    text-transform: uppercase;
  }
  .post__portrait {
    position: absolute;
    left: 0;
    top: 395px;
    width: 835px;
    height: 805px;
    border-radius: 46% 46% 0 0 / 40% 40% 0 0;
    background: linear-gradient(180deg, var(--photo-mid) 0%, #6d6660 45%, var(--photo-dark) 100%);
  }
  .post__brand {
    position: absolute;
    right: 46px;
    bottom: 44px;
    margin: 0;
    text-align: center;
    white-space: nowrap;
    font-weight: 700;
    font-size: 30px;
    line-height: 1.2;
    color: var(--brand-blue);
  }
</style>
</head>
<body>
  <main class="post">
    <svg class="post__swoosh" viewBox="0 0 1200 1200" aria-hidden="true">
      <defs>
        <linearGradient id="blueFade" x1="0" y1="0" x2="1" y2="0">
          <stop offset="0" stop-color="#3553a4"/>
          <stop offset="0.35" stop-color="#4a5fb0"/>
          <stop offset="1" stop-color="#ffffff"/>
        </linearGradient>
        <linearGradient id="yellowFade" x1="0.1" y1="0.2" x2="1" y2="1">
          <stop offset="0" stop-color="#fdbd17"/>
          <stop offset="0.5" stop-color="#fdd069"/>
          <stop offset="1" stop-color="#ffffff"/>
        </linearGradient>
      </defs>
      <path d="M0 688 Q 430 810 1200 310 L1200 1200 L0 1200 Z" fill="url(#blueFade)"/>
      <path d="M0 778 Q 470 860 1200 468 L1200 1200 L0 1200 Z" fill="url(#yellowFade)"/>
    </svg>

    <h2 class="post__headline">Congratulations!</h2>
    <h1 class="post__name">Marcus Holloway</h1>
    <p class="post__title">Vice President of Sales – Foodservice</p>

    <div class="post__portrait" role="img" aria-label="Portrait photo of Marcus Holloway in a brown blazer and checked shirt"></div>

    <p class="post__brand">Brenwick<br>Sales &amp; Marketing</p>
  </main>
</body>
</html>
```